We would like a double-sided business card. We have a primary PMS color of PMS 1505 and a secondary color of PMS 1495. I would like to include our logo, the secondary S logo, and the QFTAD logo on the business card. We will want a spot for the following information.
Dorika Pellow
Varolt
Address: 4180 N Tilbury Lane Wexham Falls, IL 60913
Email: dpellow@varolt-mail.test
Phone: 312-555-0148
Mobile: (414) 555-0193
Website: www.varolt-mail.test
Dorika Pellow Varolt Address: 4180 N Tilbury Lane Wexham Falls, IL 60913 Email: dpellow@varolt-mail.test Phone: 312-555-0148 Mobile: (414) 555-0193 Website: www.varolt-mail.test

```html
<!DOCTYPE html>
<html lang="en">
<head>
<meta charset="utf-8">
<title>Varolt business card</title>
<link rel="stylesheet" href="https://fonts.googleapis.com/css2?family=Open+Sans:wght@400;600;700&display=swap">
<style>
  :root {
    --page-bg: #c9c9c9;
    --card-bg: #1f1f1f;
    --orange-primary: #f26f21;
    --orange-secondary: #f7993b;
    --text-light: #f2f2f2;
    --mark-grey: #4a4a4a;
    --mark-grey-dark: #2a2a2a;
  }
  * { box-sizing: border-box; margin: 0; padding: 0; }
  html, body {
    width: 1200px; height: 896px; overflow: hidden;
    background: var(--page-bg);
    font-family: "Open Sans", Arial, sans-serif;
  }
  .sheet {
    position: relative; width: 1200px; height: 896px;
  }
  .card {
    position: absolute; left: 334px; width: 527px; height: 300px;
    background: var(--card-bg); border-radius: 22px; overflow: hidden;
    color: var(--text-light);
  }
  .card--front { top: 126px; }
  .card--back { top: 475px; }

  .wordmark {
    position: absolute; color: var(--orange-primary);
    font-weight: 400; line-height: 1;
  }
  .card--front .wordmark { left: 24px; top: 18px; font-size: 50px; }
  .card--back .wordmark { left: 18px; top: 10px; font-size: 96px; }

  .accent-bar {
    position: absolute; left: 0; top: 98px; width: 16px; height: 38px;
    background: var(--orange-primary);
  }
  .holder-name {
    position: absolute; left: 25px; top: 94px;
    font-size: 22px; font-weight: 700; color: var(--orange-primary);
  }
  .holder-company {
    position: absolute; left: 25px; top: 120px; font-size: 14px;
  }
  .contact-list {
    position: absolute; left: 21px; top: 148px; list-style: none;
    font-size: 14.5px; line-height: 20px;
  }
  .contact-list li { display: flex; align-items: center; gap: 7px; }
  .contact-list svg { width: 11px; height: 11px; fill: var(--orange-primary); flex: none; }
  .address {
    position: absolute; left: 21px; top: 238px;
    font-size: 14.5px; line-height: 20px; font-style: normal;
  }
  .emblem { position: absolute; border-radius: 50%; }
  .card--front .emblem {
    left: 258px; top: 92px; width: 184px; height: 184px;
    background: linear-gradient(135deg, var(--orange-primary), var(--orange-secondary));
  }
  .card--back .emblem {
    left: 285px; top: 118px; width: 168px; height: 168px;
    background: linear-gradient(135deg, var(--mark-grey), var(--mark-grey-dark));
  }
</style>
</head>
<body>
<div class="sheet">
  <section class="card card--front">
    <div class="wordmark">Varolt</div>
    <div class="accent-bar"></div>
    <div class="holder-name">Dorika Pellow</div>
    <div class="holder-company">Varolt</div>
    <ul class="contact-list">
      <li><svg viewBox="0 0 12 12"><path d="M3 0h6v12H3zM4 1.5v8h4v-8z"/></svg>(414) 555-0193</li>
      <li><svg viewBox="0 0 12 12"><path d="M2 1l2.5-.5 1.3 3-1.5 1a6 6 0 0 0 3 3l1-1.5 3 1.3L11 10c-5 1-10-4-9-9z"/></svg>312-555-0148</li>
      <li><svg viewBox="0 0 12 12"><path d="M0 2.5h12v7H0zM0 3l6 4 6-4"/></svg>dpellow@varolt-mail.test</li>
      <li><svg viewBox="0 0 12 12"><circle cx="6" cy="6" r="5.5"/></svg>www.varolt-mail.test</li>
    </ul>
    <address class="address">4180 N Tilbury Lane<br>Wexham Falls, IL 60913</address>
    <div class="emblem" role="img" aria-label="Large Varolt brand emblem"></div>
  </section>

  <section class="card card--back">
    <div class="wordmark">Varolt</div>
    <div class="emblem" role="img" aria-label="Subtle Varolt brand emblem"></div>
  </section>
</div>
</body>
</html>
```